Bramwell Resources Ltd. - Refreshed business card challenge

A revised, refreshed business card design for my oil and gas company using my existing logo. Feel free to be as creative as you like!

Target Market(s)

bankers, lawyers

Industry/Entity Type

Oil And Gas Exploration

Contact Information for Business Card

See the "Must Haves" section

Font styles to use
Serif
Sans Serif

Colors

Designer to choose colors to be used in the design.

Requirements
Must have
• Existing business logo, name, title, email, phone number, business address
• Neil Hadley, CA, CPA
• Vice President Finance & Chief Financial Officer
• nhadley@bramwellresources-mail.com
• office: (587)555-0142
• cell: (403)555-0187
• 1400, 815 4 Street S.W.
• Calgary, AB
• T2P 4K8
Should not have
• Should not be plain and boring.

```html
<!DOCTYPE html>
<html lang="en">
<head>
<meta charset="utf-8">
<title>Bramwell Resources – Business Card</title>
<link href="https://fonts.googleapis.com/css2?family=Montserrat:wght@400;500;600;700;800;900&display=swap" rel="stylesheet">
<style>
  :root {
    --forest: #0d5233;
    --forest-deep: #0a4429;
    --bark: #5e3a22;
    --paper: #ffffff;
    --stage: #1d1d1d;
  }
  * { box-sizing: border-box; margin: 0; padding: 0; }
  html, body {
    width: 1200px; height: 900px; overflow: hidden;
    background: var(--stage);
    font-family: "Montserrat", sans-serif;
  }
  .canvas {
    width: 1200px; height: 900px;
    display: flex; flex-direction: column; align-items: center; justify-content: center;
    gap: 44px;
  }
  .card {
    width: 560px; height: 320px;
    position: relative;
  }
  .card-front {
    background: var(--forest);
    display: flex; align-items: center; justify-content: center;
  }
  .front-brand {
    display: flex; align-items: center; gap: 14px;
    color: var(--paper);
  }
  .front-brand .mark {
    width: 18px; height: 18px; background: var(--paper);
  }
  .front-brand .brand-name {
    font-weight: 800; font-size: 34px; letter-spacing: 0.5px;
  }
  .card-back {
    background: var(--paper);
    border: 8px solid var(--forest);
    display: flex; align-items: center;
  }
  .back-brand {
    width: 245px; padding-left: 40px;
    color: var(--forest);
    font-weight: 800; font-size: 30px; line-height: 1.05;
  }
  .divider {
    position: absolute; left: 262px; top: 34px; bottom: 34px;
    width: 3px; display: flex; flex-direction: column; gap: 14px;
  }
  .divider span { flex: 1; background: var(--forest); }
  .divider span.mid { background: var(--bark); }
  .details {
    padding-left: 36px;
    display: flex; flex-direction: column; gap: 14px;
    font-size: 12.5px; line-height: 1.35;
  }
  .person-name {
    color: var(--forest); font-weight: 700; font-size: 23px; line-height: 1.1;
  }
  .credentials {
    color: var(--bark); font-weight: 500; font-size: 11px; margin-left: 4px;
  }
  .person-title { color: var(--bark); font-weight: 500; }
  .address { color: var(--forest); font-weight: 500; }
  .contact .phone { color: var(--bark); font-weight: 500; }
  .contact .email, .contact .web { color: var(--forest); font-weight: 600; }
</style>
</head>
<body>
<main class="canvas">
  <section class="card card-front">
    <div class="front-brand">
      <span class="mark"></span>
      <span class="brand-name">Bramwell Resources</span>
    </div>
  </section>

  <section class="card card-back">
    <div class="back-brand">Bramwell<br>Resources</div>
    <div class="divider"><span></span><span class="mid"></span><span></span></div>
    <div class="details">
      <div>
        <div class="person-name">Neil Hadley<span class="credentials">CA | CPA</span></div>
        <div class="person-title">Vice President Finance &amp;<br>Chief Financial Officer</div>
      </div>
      <div class="address">1400, 815 4 Street S.W.<br>Calgary, AB, T2P 4K8</div>
      <div class="contact">
        <div class="phone">(587)555-0142</div>
        <div class="phone">(403)555-0187</div>
        <div class="email">nhadley@bramwellresources-mail.com</div>
        <div class="web">www.bramwellresources-mail.com</div>
      </div>
    </div>
  </section>
</main>
</body>
</html>
```